Boutique Salon Brand Refresh needs color palette, font, templates.

Toveli Hair Studio is an established hair salon celebrating 10 years in business. We are currently evolving our brand to better reflect who we are today, the clients we serve, and the direction we want to take our business moving forward.
Our goal is to position Toveli as a refined, modern boutique salon created specifically for “The Toveli Woman.”
In the past, much of our branding and marketing focused on us—our salon, our space, our services, and our team. Going forward, we want to shift that focus to her: who she is, what she values, how she wants to look and feel, and how Toveli fits into her life.
We want our brand to communicate expertise and quality without feeling overly luxurious, trendy, intimidating, or impersonal. It should feel polished, sophisticated, warm, approachable, and timeless—a boutique experience designed for women who value beautiful, healthy hair and trusted professional guidance.
As part of this rebrand, we are looking to establish a cohesive visual identity that can be carried consistently across our website, social media, email marketing, print materials, signage, and other client touchpoints.

*** For THIS PROJECT, we are SPECIFICALLY LOOKING for:
- A cohesive brand color palette
- 2–3 complementary fonts for consistent use across our marketing
- 4–5 customizable social media templates that can be used across Instagram and Facebook
A visual direction that feels distinctive to Toveli and speaks directly to The Toveli Woman.
The following information provides more detail about The Toveli Woman, our positioning, brand personality, values, and the overall direction we envision for the next chapter of Toveli Hair Studio.
Toveli Hair Studio
Brookvale, NJ USA
tovelihairbrookvale.example

--PRIMARY AUDIENCE
The Toveli woman values quality, consistency, and professional guidance.
She wants to look polished and current without appearing overdone or overly trendy.
She may be managing grey hair, changing texture, thinning, dryness, fading color, or a style that no longer reflects who she is. She wants an expert who understands these concerns and can create a realistic plan.
She is willing to invest in professional services and products when she understands their value.
She does not want to experiment with her appearance.
She wants to feel confident in the person caring for her hair.
Women approximately 45 to 65 years old living in Mendham, Morris County, and surrounding communities.

--COLOR PALETTE
The overall appearance should feel calm, spacious, editorial, and cohesive. The entire visual system should feel more like a refined boutique hotel, skincare brand, or luxury lifestyle publication than a traditional salon advertisement.
When choosing the palette, we want the colors to invoke these feelings.
Represents:
Expertise
Confidence
Timelessness
Professionalism
Calm
Warmth
Cleanliness
Soft luxury
Natural beauty
Warmth
Balance
Subtle sophistication
Consistency

--TYPOGRAPHY
The typography system should feel refined, modern, readable, and timeless.
Recommended usage for each font, size, spacing, etc.

----TEMPLATE IDEAS
**EDUCATIONAL POST
Frequently asked questions
Healthy-hair advice
Healthy Hair Tip
Grey Coverage FAQ
Grey Blending FAQ
Product education
Single-tip graphic
**REVIEWS
Google reviews
Finest of Brookvale recognition/Community awards
Long-term guest relationships
Guest testimonials/satisfaction stories
Referral stories
**ADS
**SALON UPDATES/INFO
Holiday hours
Policy reminder
New guest guide
Consultation invitation
Service spotlight
Seasonal guidance
**ABOUT TOVELI
Who we are
What to expect from us
What we can provide
Our expertise
**HIGHLIGHT ICON
Questions
Testimonial
Product
Reminders

TEMPLATE RULES
Use the color palette
Use only the font system
Maintain generous spacing
Limit text
Use consistent margins
Keep calls to action simple
Avoid crowded layouts
Use photography intentionally
Keep every template recognizably Toveli

Target Market(s)

Women approximately 45 to 65 years old living in Mendham, Morris County, and surrounding communities. She values quality, consistency, and professional guidance. She wants to look polished and current without appearing overdone or overly trendy. She is willing to invest in professional services and products when she understands their value.

Industry/Entity Type

Hair Salon

Font styles to use
Serif
Sans Serif
Script

Requirements
Must have
• We are looking to establish a cohesive visual identity that can be carried consistently across platforms. It should communicate expertise and quality without feeling overly fluffy, trendy, intimidating, or impersonal. I would like to see multiple template ideas. Example- one template for education post, one template for reviews, one for salon information/updates. etc. My main goal here is to simplify social media posts by having designated templates for each post category. WE WILL BE KEEPING OUR ORGINAL LOGO- SO COLOR PALETTE MUST REFLECT THAT.
Nice to have
• Color palette and font sets that reflect the brand. **cohesive visual identity**
Should not have
• Nothing flashy, busy, overly trendy.

```html
<!DOCTYPE html>
<html lang="en">
<head>
<meta charset="utf-8">
<title>Toveli Hair Studio — Social Templates</title>
<link href="https://fonts.googleapis.com/css2?family=Playfair+Display:wght@400;500&family=Outfit:wght@400;500;600;700&display=swap" rel="stylesheet">
<style>
:root{
  --page:#e8e8e8;
  --cream:#f3f0ea;
  --olive:#63634f;
  --maroon:#7a2226;
  --ink:#1d1b19;
  --tan:#8c6e5e;
  --white:#ffffff;
}
*{margin:0;padding:0;box-sizing:border-box}
html,body{width:1028px;height:1200px;overflow:hidden;background:var(--page)}
body{position:relative;font-family:'Outfit',sans-serif;color:var(--ink)}
h2{font-weight:400}

.post{position:absolute;width:421px;height:421px;background:var(--cream);overflow:hidden;
  box-shadow:0 14px 12px -12px rgba(0,0,0,.28)}
.post--review{left:74px;top:84px}
.post--welcome{left:533px;top:84px}
.post--ad{left:74px;top:553px}
.post--faq{left:533px;top:553px}
.abs{position:absolute}
.center{left:0;right:0;text-align:center}
.torn{position:absolute;left:0;bottom:0;width:421px;height:36px}

.wordmark{font-family:'Playfair Display',serif;font-weight:400;line-height:1;text-align:center}

/* review */
.quote-mark{top:70px;font-family:'Playfair Display',serif;font-size:150px;line-height:1;color:var(--maroon);font-weight:500}
.stars{top:166px;font-size:17px;letter-spacing:9px;color:var(--maroon);padding-left:9px}
.review-text{top:200px;font-family:'Playfair Display',serif;font-size:21px;line-height:24px;color:var(--ink)}
.review-name{top:312px;font-size:12px;font-weight:600;color:var(--maroon)}
.swash{position:absolute}

/* welcome */
.welcome-mark{top:52px;font-size:28px;color:var(--ink)}
.welcome-title{top:134px;font-family:'Playfair Display',serif;font-size:31px;line-height:40px;color:var(--maroon)}
.welcome-sub{top:184px;font-size:11.5px;line-height:13.5px}
.welcome-body{top:253px;font-size:11.5px;line-height:13.5px}
.btn{position:absolute;left:109px;top:304px;width:203px;height:25px;border-radius:13px;background:var(--maroon);
  color:var(--white);font-size:11.5px;letter-spacing:.4px;display:flex;align-items:center;justify-content:center}
.place{top:341px;font-size:10.5px}
.url{display:flex;align-items:center;gap:4px;font-size:10.5px}
.url svg{width:11px;height:11px;flex:none}

/* ad */
.ad-top{left:0;top:0;width:421px;height:215px}
.ad-photo{left:0;top:80px;width:184px;height:341px;
  background:radial-gradient(ellipse at 45% 40%,#c9a088 0%,#8a5634 45%,#5a3320 75%,#e7dccd 100%)}
.ad-copy{z-index:2}
.ad-title{left:198px;top:64px;font-family:'Playfair Display',serif;font-size:30px;line-height:32.5px;color:var(--white)}
.ad-body{left:197px;top:227px;width:150px;font-size:11px;line-height:13.5px}
.ad-tags{left:197px;top:295px;font-size:10.5px;line-height:17px;font-weight:700;color:var(--tan);letter-spacing:.3px}
.ad-url{left:197px;top:375px;color:var(--tan);font-size:8.5px;gap:3px}
.ad-url svg{width:9px;height:9px}
.ad-mark{left:338px;top:358px;font-size:13px;color:var(--ink);width:68px}

/* faq */
.faq-side{left:0;top:0;width:421px;height:421px}
.faq-mark{left:300px;top:52px;width:110px;font-size:22px;color:var(--white)}
.faq-title{left:31px;top:76px;font-family:'Playfair Display',serif;font-size:28px;line-height:34px;color:var(--olive)}
.faq-q{left:34px;top:152px;font-size:9.8px;line-height:12.5px;font-weight:700;width:200px}
.faq-a{left:34px;top:178px;font-size:9.8px;line-height:14.4px;width:215px}
.faq-q b,.faq-a b{position:absolute;left:0}
.faq-q span,.faq-a span{display:block;padding-left:14px}
.faq-cta{left:29px;top:338px;width:353px;height:25px;border-radius:13px;background:var(--maroon);color:var(--white);
  font-size:14px;font-weight:600;font-style:italic;display:flex;align-items:center;justify-content:center}
.faq-url{left:50px;top:383px}

/* highlight icons */
.highlight{position:absolute;top:1039px;width:120px;text-align:center}
.highlight svg{width:66px;height:66px;display:block;margin:0 auto}
.highlight span{display:block;margin-top:20px;font-size:14px;letter-spacing:.2px}
</style>
</head>
<body>

<svg width="0" height="0" style="position:absolute">
  <defs>
    <symbol id="globe" viewBox="0 0 12 12"><g fill="none" stroke="currentColor" stroke-width="1"><circle cx="6" cy="6" r="5.2"/><ellipse cx="6" cy="6" rx="2.3" ry="5.2"/><line x1=".8" y1="6" x2="11.2" y2="6"/><line x1="1.6" y1="3.4" x2="10.4" y2="3.4"/><line x1="1.6" y1="8.6" x2="10.4" y2="8.6"/></g></symbol>
  </defs>
</svg>

<!-- Review template -->
<section class="post post--review">
  <div class="abs center quote-mark">&ldquo;</div>
  <div class="abs center stars">★★★★★</div>
  <p class="abs center review-text">&ldquo;Toveli has completely<br>changed the way I feel<br>about my hair.&rdquo;</p>
  <svg class="swash" style="left:123px;top:297px" width="178" height="8" viewBox="0 0 178 8"><path d="M0 5 Q90 -1 178 3 Q90 1 0 6Z" fill="var(--maroon)"/></svg>
  <p class="abs center review-name">-Clara Whitfield</p>
  <svg class="torn" viewBox="0 0 421 36" preserveAspectRatio="none"><path d="M0 5 L18 3 L30 8 L48 4 L64 9 L80 5 L98 10 L115 6 L132 11 L150 7 L170 10 L188 4 L205 9 L224 6 L240 11 L258 5 L276 9 L294 4 L312 8 L330 3 L348 7 L366 2 L384 6 L402 3 L421 6 L421 36 L0 36Z" fill="var(--olive)"/></svg>
</section>

<!-- Consultation invitation template -->
<section class="post post--welcome">
  <div class="abs center wordmark welcome-mark">The Toveli Woman</div>
  <h2 class="abs center welcome-title">NEW TO TOVELI?</h2>
  <p class="abs center welcome-sub">Your hair journey<br>starts with a conversation.</p>
  <svg class="swash" style="left:129px;top:224px" width="178" height="8" viewBox="0 0 178 8"><path d="M0 5 Q90 -1 178 3 Q90 1 0 6Z" fill="var(--maroon)"/></svg>
  <p class="abs center welcome-body">Let's talk about your hair, your goals<br>and what feels right for you</p>
  <div class="btn">BOOK YOUR CONSULTATION</div>
  <p class="abs center place">Brookvale, NJ</p>
  <div class="abs center url" style="top:362px;justify-content:center"><svg><use href="#globe"/></svg>tovelihairbrookvale.example</div>
  <svg class="torn" viewBox="0 0 421 36" preserveAspectRatio="none"><path d="M0 10 L20 6 L38 12 L56 8 L74 13 L92 7 L110 12 L130 8 L148 13 L166 9 L186 12 L204 6 L222 11 L240 7 L258 12 L276 6 L296 10 L314 5 L332 9 L352 4 L370 8 L390 3 L406 7 L421 4 L421 36 L0 36Z" fill="var(--olive)"/></svg>
</section>

<!-- Ad template -->
<section class="post post--ad">
  <svg class="abs ad-top" viewBox="0 0 421 215" preserveAspectRatio="none"><path d="M0 0 H421 V206 L404 208 L386 203 L366 209 L346 204 L326 210 L306 205 L286 210 L266 204 L246 209 L226 203 L206 207 L0 207Z" fill="var(--olive)"/></svg>
  <div class="abs ad-photo" role="img" aria-label="Portrait photograph of a woman with long glossy brown wavy hair, looking down to the side"></div>
  <h2 class="abs ad-copy ad-title">BEAUTIFUL<br>HAIR<br>STARTS<br>WITH A PLAN.</h2>
  <p class="abs ad-copy ad-body">At Toveli, we take the time<br>to understand your hair,<br>your lifestyle,<br>and your goals.</p>
  <p class="abs ad-copy ad-tags">EXPERT GUIDANCE.<br>PERSONALIZED CARE.<br>BEAUTIFUL RESULTS.</p>
  <div class="abs ad-copy url ad-url"><svg><use href="#globe"/></svg>tovelihairbrookvale.example</div>
  <div class="abs ad-copy wordmark ad-mark">The Toveli Woman</div>
</section>

<!-- FAQ template -->
<section class="post post--faq">
  <svg class="abs faq-side" viewBox="0 0 421 421" preserveAspectRatio="none"><path d="M267 0 H421 V421 H266 L270 395 L264 370 L271 340 L265 305 L272 270 L266 240 L273 205 L267 170 L274 135 L268 100 L274 70 L267 40 L273 18Z" fill="var(--olive)"/></svg>
  <div class="abs wordmark faq-mark">The Toveli<br>Woman</div>
  <h2 class="abs faq-title">FREQUENTLY<br>ASKED</h2>
  <p class="abs faq-q"><b>Q:</b><span>How do I know which color service is right for me?</span></p>
  <p class="abs faq-a"><b>A:</b><span>It starts with a consultation. Our stylists take the time to understand your hair history, lifestyle, maintenance preferences, and desired result before recommending a service. Whether you're looking to refresh your color, add dimension, brighten your hair, or blend your natural gray, we'll help you find an approach that feels realistic and right for you.</span></p>
  <div class="abs faq-cta">Let's create a plan for your hair.</div>
  <div class="abs url faq-url"><svg><use href="#globe"/></svg>tovelihairbrookvale.example</div>
</section>

<!-- Highlight icons -->
<div class="highlight" style="left:262px">
  <svg viewBox="0 0 66 66"><circle cx="33" cy="33" r="33" fill="var(--maroon)"/><circle cx="33" cy="33" r="27" fill="none" stroke="var(--white)" stroke-width="1.6"/><text x="33" y="45" text-anchor="middle" font-family="Playfair Display,serif" font-size="34" font-weight="500" fill="var(--white)">?</text></svg>
  <span>Questions</span>
</div>
<div class="highlight" style="left:390px">
  <svg viewBox="0 0 66 66"><circle cx="33" cy="33" r="33" fill="var(--maroon)"/><circle cx="33" cy="33" r="27" fill="none" stroke="var(--white)" stroke-width="1.6"/><g fill="none" stroke="var(--white)" stroke-width="1.8" stroke-linejoin="round"><rect x="31" y="14" width="4" height="5"/><path d="M29 19 H37 V23 H29Z"/><rect x="26" y="24" width="14" height="24" rx="3"/></g></svg>
  <span>Products</span>
</div>
<div class="highlight" style="left:517px">
  <svg viewBox="0 0 66 66"><circle cx="33" cy="33" r="33" fill="var(--maroon)"/><circle cx="33" cy="33" r="27" fill="none" stroke="var(--white)" stroke-width="1.6"/><text x="33" y="66" text-anchor="middle" font-family="Playfair Display,serif" font-size="62" font-weight="500" fill="var(--white)">&ldquo;</text></svg>
  <span>Testemonials</span>
</div>
<div class="highlight" style="left:643px">
  <svg viewBox="0 0 66 66"><circle cx="33" cy="33" r="33" fill="var(--maroon)"/><circle cx="33" cy="33" r="27" fill="none" stroke="var(--white)" stroke-width="1.6"/><g fill="none" stroke="var(--white)" stroke-width="1.8" stroke-linejoin="round"><path d="M33 16 C25 16 22 22 22 29 V37 L18 42 H48 L44 37 V29 C44 22 41 16 33 16Z"/><path d="M29 45 Q33 50 37 45"/></g></svg>
  <span>Reminders</span>
</div>

</body>
</html>
```